I need a business card design for a new dance business. I offer classical Indian dance tuition and also professional performances. I want to offer the community a variety of Indian dance experiences which include: group class and private tuition, school and preschool educational courses and workshops. dance theatre performances, community function workshops and performances, Kids Bollywood parties, wedding & conference performances, mouth percussion classes, Indian mythology/ dance costume and make up workshops.
The final design should communicate a feeling and impression of the vibrance and energy of Indian dance.
Updates
Hi Everyone,
Project Deadline Extended
Reason: I would like to refine a few changes to the details of this lovely design and we have run out of time!
Project Deadline Extended
Reason: Still waiting to hear back form designer re two possible changes to the card design. Tomorrow is the deadline and I have sent several messages but with no response. I need to see this through before selecting this lovely design.
Thank you.
Tara
Industry/Entity Type
Preschool
Requirements
Must have
- The front of the business card should have the photo of me (my face and torso), surrounded entirely by a border of bright magenta (to match the magenta of my lipstick - it is the same as the magenta on my skirt in the second photo). Within the top border I want (perhaps yellow-gold) writing to say "Tara Holloway - Artistic Director" and within the bottom border it should read "Silver Creek Kathak Studio." If you turn the card on its side the left border should have my telephone number: 0417 826 394 and the right-hand border should read: silvercreekkathakstudio@fernmail.example
The reverse of the card should be the orange of the dance costume
and I'd like the picture of my feet and legs to be on the right side of the back of the card as a side border. Centre-aligned on the orange background it should read (perhaps in dark magenta):
Indian dance classes + private tuition
School + preschool educational courses and workshops
Dance theatre performances
Community function workshops and performances
Children's Bollywood parties
Wedding + conference performances
Mouth percussion classes
Indian mythology and dance demonstration workshops
Dance costume and make-up workshops
Nice to have
- A lovely artistic but easy-to-read font would be nice.

```html
<!DOCTYPE html>
<html lang="en">
<head>
<meta charset="utf-8">
<title>Silver Creek Kathak Studio — Business Card</title>
<link rel="stylesheet" href="https://fonts.googleapis.com/css2?family=Kaushan+Script&display=swap">
<style>
  :root {
    --page: #ffffff;
    --magenta: #b900d6;
    --gold: #f6c21c;
    --orange: #f8a100;
    --deep-magenta: #a4109c;
    --script: "Kaushan Script", cursive;
  }
  html, body {
    margin: 0;
    padding: 0;
    width: 1200px;
    height: 504px;
    overflow: hidden;
    background: var(--page);
  }
  .canvas {
    position: relative;
    width: 1200px;
    height: 504px;
  }
  .card {
    position: absolute;
    top: 159px;
    width: 550px;
    height: 316px;
    overflow: hidden;
    font-family: var(--script);
  }
  .card-front { left: 26px; background: var(--magenta); color: var(--gold); }
  .card-back { left: 620px; background: var(--orange); color: var(--deep-magenta); }

  .studio-name {
    position: absolute;
    top: 14px;
    right: 18px;
    margin: 0;
    font-size: 21px;
    font-weight: 400;
  }
  .person-name {
    position: absolute;
    top: 50px;
    left: 20px;
    margin: 0;
    font-size: 17px;
  }
  .person-role {
    position: absolute;
    top: 78px;
    left: 20px;
    margin: 0;
    font-size: 16px;
  }
  .contact-phone {
    position: absolute;
    top: 260px;
    left: 20px;
    margin: 0;
    font-size: 16px;
  }
  .contact-email {
    position: absolute;
    top: 288px;
    left: 20px;
    margin: 0;
    font-size: 14px;
  }
  .dancer-portrait {
    position: absolute;
    left: 262px;
    top: 42px;
    width: 288px;
    height: 274px;
    background: radial-gradient(ellipse at 50% 45%, #f0c9b0 0%, #d58f5a 35%, #c36a16 60%, rgba(185,0,214,0) 78%);
  }

  .services {
    position: absolute;
    top: 28px;
    left: 11px;
    margin: 0;
    padding: 0;
    list-style: none;
    font-size: 14.5px;
    line-height: 28.3px;
    white-space: nowrap;
  }
  .dancer-feet {
    position: absolute;
    right: 0;
    top: 0;
    width: 200px;
    height: 316px;
    background: linear-gradient(90deg, rgba(248,161,0,0) 0%, #c21ab8 30%, #9b0aa3 55%, #d98a1a 80%, rgba(248,161,0,0) 100%);
  }
</style>
</head>
<body>
<main class="canvas">
  <section class="card card-front">
    <div class="dancer-portrait" role="img" aria-label="Photograph of the dancer in classical costume, face and torso"></div>
    <h1 class="studio-name">Silver Creek Kathak Studio</h1>
    <p class="person-name">Tara Holloway</p>
    <p class="person-role">Artistic Director</p>
    <p class="contact-phone">Ph: 0417 826 394</p>
    <p class="contact-email">silvercreekkathakstudio@fernmail.example</p>
  </section>

  <section class="card card-back">
    <ul class="services">
      <li>Indian dance classes + private tuition</li>
      <li>Dance theatre performances</li>
      <li>Children's Bollywood parties</li>
      <li>Wedding + conference performances</li>
      <li>Mouth percussion classes</li>
      <li>Community function workshops and performances</li>
      <li>School + preschool educational courses and workshops</li>
      <li>Indian mythology and dance demonstration workshops</li>
      <li>Dance costume and make-up workshops</li>
    </ul>
    <div class="dancer-feet" role="img" aria-label="Photograph of the dancer's legs and feet in a magenta and orange costume"></div>
  </section>
</main>
</body>
</html>
```